Business Card Design Project

We need a business card design for a new company based in New York called "Marble Fox's". We do major installations of energy saving devices primarily LED lighting in large facilities. We would like a double sided card with our contact info on one side with our logo (to be designed) and on the other side the services we provide. We would like a heavy weight glossy card using the colors green and white. The final design should communicate environmental soundness and our market is very upscale corporations.
We would like our logo to illustrate LED lighting and we were thinking if we could get a stock picture of the Corliss Vane Building lit up on July 4th with red, white and blue LED lighting. The alternative would be anything that connotes environmentally proper thinking. It could be either a picture or a design.

```html
<!DOCTYPE html>
<html lang="en">
<head>
<meta charset="utf-8">
<title>Marble Fox's – Business Card</title>
<link rel="stylesheet" href="https://fonts.googleapis.com/css2?family=Jost:wght@300&family=Tinos&display=swap">
<style>
  :root {
    --card-black: #000000;
    --divider-grey: #8c8c8c;
    --ink-white: #ffffff;
    --glow-red: #c8321e;
    --glow-orange: #d98024;
    --glow-cream: #e6d6bc;
    --glow-green: #2f9a48;
    --glow-blue: #2a4fc0;
    --glow-violet: #7a38c0;
  }
  * { margin: 0; padding: 0; box-sizing: border-box; }
  html, body {
    width: 1200px; height: 1000px; overflow: hidden;
    background: var(--card-black);
  }
  .canvas { position: relative; width: 1200px; height: 1000px; background: var(--card-black); }
  .card-side { position: absolute; left: 0; width: 1200px; background: var(--card-black); }
  .card-front { top: 0; height: 524px; }
  .card-back { top: 533px; height: 467px; }
  .divider { position: absolute; left: 0; top: 524px; width: 1200px; height: 9px; background: var(--divider-grey); }

  .brand-name {
    font-family: "Jost", "Futura", sans-serif;
    font-weight: 300;
    color: var(--ink-white);
    font-size: 108px;
    line-height: 1;
    letter-spacing: -1px;
    white-space: nowrap;
  }
  .brand-tagline {
    font-family: "Jost", "Futura", sans-serif;
    font-weight: 300;
    color: var(--ink-white);
    font-size: 34px;
    letter-spacing: 20px;
    line-height: 1;
    white-space: nowrap;
  }
  .card-front .brand-name { position: absolute; left: 192px; top: 202px; }
  .card-front .brand-tagline { position: absolute; left: 322px; top: 322px; }

  .night-photo {
    position: absolute; left: 740px; top: 0; width: 290px; height: 470px;
    background: linear-gradient(90deg, var(--glow-violet) 0%, var(--glow-red) 22%, var(--glow-orange) 42%, var(--glow-cream) 55%, var(--glow-green) 75%, var(--glow-blue) 100%);
    -webkit-mask-image: radial-gradient(ellipse 50% 48% at 50% 52%, rgba(0,0,0,0.85) 0%, rgba(0,0,0,0.4) 55%, rgba(0,0,0,0) 100%);
    mask-image: radial-gradient(ellipse 50% 48% at 50% 52%, rgba(0,0,0,0.85) 0%, rgba(0,0,0,0.4) 55%, rgba(0,0,0,0) 100%);
  }

  .card-back .brand-block { position: absolute; left: 0; top: 50px; width: 1170px; text-align: center; }
  .card-back .brand-tagline { display: block; margin-top: 6px; padding-left: 20px; }

  .contact-list {
    position: absolute; left: 0; top: 262px; width: 1170px;
    list-style: none; text-align: center;
    font-family: "Tinos", "Times New Roman", serif;
    color: var(--ink-white);
    font-size: 27px;
    letter-spacing: 3.5px;
    line-height: 35px;
  }
</style>
</head>
<body>
<main class="canvas">
  <section class="card-side card-front">
    <h1 class="brand-name">Marble Fox's</h1>
    <p class="brand-tagline">pay off</p>
    <div class="night-photo" role="img" aria-label="Night photograph of the top of the Corliss Vane Building lit in rainbow LED colours"></div>
  </section>

  <div class="divider"></div>

  <section class="card-side card-back">
    <div class="brand-block">
      <h2 class="brand-name">Marble Fox's</h2>
      <span class="brand-tagline">pay off</span>
    </div>
    <ul class="contact-list">
      <li>Via Lorenzo Brina 218/7</li>
      <li>16149 Genova, Italy</li>
      <li>email: hello@marblefox.com</li>
      <li>website: glowpathled.com</li>
      <li>Tel. 010 482731650</li>
    </ul>
  </section>
</main>
</body>
</html>
```